Packaging box design for start up candle company based in Sydney Australia

I need an eye catching box design for my candle company called Morningside Wickery. We specialise only in delicious cake and cocktail scented candles. I want to convey a sense of elegant whimsy.
I have a logo and a style guide which I'm happy with, but need to complete the brand with a stunning box design.
I'd like the same design for two different sized boxes.

```html
<!DOCTYPE html>
<html lang="en">
<head>
<meta charset="utf-8">
<title>Morningside Wickery – Sydney Box</title>
<link href="https://fonts.googleapis.com/css2?family=Lora:wght@400&family=Montserrat:wght@400&display=swap" rel="stylesheet">
<style>
  :root {
    --canvas: #f2f2f2;
    --board: #cdd6d9;
    --label: #d1dadd;
    --ink: #1f1d1e;
    --frame: #262425;
    --skyline: #b9bfc1;
    --art-teal: #5f8f90;
    --art-pink: #e7a2c0;
    --art-purple: #a67fb8;
    --art-charcoal: #3d3f42;
    --art-rust: #b9573f;
    --art-sand: #b59a86;
  }
  * { margin: 0; padding: 0; box-sizing: border-box; }
  html, body {
    width: 1184px;
    height: 1200px;
    overflow: hidden;
    background: var(--canvas);
  }
  .box-front {
    position: absolute;
    left: 115px;
    top: 40px;
    width: 955px;
    height: 1120px;
    background: var(--board);
  }
  .painted-panel {
    position: absolute;
    left: 45px;
    top: 145px;
    width: 865px;
    height: 850px;
    background:
      linear-gradient(180deg, rgba(95,143,144,0.85) 0%, rgba(166,127,184,0.6) 22%, rgba(231,162,192,0.8) 50%, rgba(181,154,134,0.75) 78%, rgba(61,63,66,0.9) 100%),
      linear-gradient(90deg, var(--art-charcoal) 0%, var(--art-pink) 40%, var(--art-teal) 70%, var(--art-rust) 100%);
  }
  .label {
    position: absolute;
    left: 135px;
    top: 275px;
    width: 685px;
    height: 635px;
    background: var(--label);
    border: 8px solid var(--frame);
  }
  .brand-name {
    position: absolute;
    top: 88px;
    left: 0;
    width: 100%;
    text-align: center;
    font-family: 'Lora', serif;
    font-weight: 400;
    font-size: 34px;
    line-height: 1.15;
    letter-spacing: 5px;
    color: var(--ink);
    text-transform: uppercase;
  }
  .skyline {
    position: absolute;
    left: 60px;
    top: 235px;
    width: 555px;
    height: 105px;
  }
  .city-name {
    position: absolute;
    top: 290px;
    left: 0;
    width: 100%;
    text-align: center;
    font-family: 'Lora', serif;
    font-weight: 400;
    font-size: 118px;
    line-height: 1;
    color: var(--ink);
  }
  .product-line {
    position: absolute;
    bottom: 24px;
    left: 0;
    width: 100%;
    text-align: center;
    font-family: 'Montserrat', sans-serif;
    font-size: 22px;
    color: var(--ink);
  }
</style>
</head>
<body>
  <main class="box-front">
    <div class="painted-panel" role="img" aria-label="Abstract painted brush-stroke artwork in pink, teal, purple, charcoal and rust"></div>
    <section class="label">
      <h1 class="brand-name">Morningside<br>Wickery</h1>
      <div class="skyline" role="img" aria-label="Faint silhouette of the Sydney city skyline with harbour bridge and opera house">
        <svg width="555" height="105" viewBox="0 0 555 105" aria-hidden="true">
          <rect x="0" y="45" width="555" height="60" fill="var(--skyline)" opacity="0.55"/>
        </svg>
      </div>
      <h2 class="city-name">Sydney</h2>
      <p class="product-line">Cocktail Scented Candles</p>
    </section>
  </main>
</body>
</html>
```